custom carpentry, woodworking and home repair company needs logo design and business card design

Attention: I apologize but I just received notification from my state that I cannot use the company name that I originally submitted (Joinolux). The new name will be Joinolux We need a company logo and business card design for our new company based in the Hampton Roads area of Virginia. The company name is Joinolux. The final design should give a first impression of true craftsmanship and attention to detail. We would like the card to include the company name, my name Mark Tellman (owner), phone number (757) 348-2615, website (joinolux-example.com) and email address (mark@joinolux-example.com). Everything else is up to your discretion. Thanks, have fun, and good luck.

Industry/Entity Type

Business

Contact Information for Business Card

See project description

Logo Text

see project description

Colors

Designer to choose colors to be used in the design.

```html
<!DOCTYPE html>
<html lang="en">
<head>
<meta charset="utf-8">
<title>Joinolux — Business Card</title>
<link href="https://fonts.googleapis.com/css2?family=Roboto:wght@400;700;900&display=swap" rel="stylesheet">
<style>
  :root {
    --stage: #1c1c1c;
    --card-white: #f4f4f4;
    --ink: #151515;
    --gold: #d9a21f;
    --amber-top: #e6bb3c;
    --amber-bottom: #e9861f;
  }
  * { box-sizing: border-box; margin: 0; padding: 0; }
  html, body { width: 1200px; height: 900px; overflow: hidden; }
  body {
    background: var(--stage);
    font-family: "Roboto", Arial, sans-serif;
    display: flex;
    align-items: center;
    justify-content: center;
    gap: 48px;
  }
  .card {
    position: relative;
    width: 525px;
    height: 300px;
    border-radius: 26px;
    overflow: hidden;
    flex: none;
  }
  .card-front { background: var(--card-white); color: var(--ink); }
  .card-back {
    background: linear-gradient(160deg, var(--amber-top) 0%, #eab54a 45%, var(--amber-bottom) 100%);
    display: flex; align-items: center; justify-content: center;
  }
  .brand-name {
    font-weight: 900;
    color: var(--ink);
    text-transform: uppercase;
    line-height: 1;
    letter-spacing: -0.5px;
    white-space: nowrap;
  }
  .card-front .brand-name {
    position: absolute; left: 40px; top: 82px; font-size: 44px;
  }
  .card-back .brand-name { font-size: 72px; }
  .divider {
    position: absolute; left: 262px; top: 96px;
    width: 2px; height: 96px; background: var(--ink);
  }
  .contact {
    position: absolute; left: 280px; top: 92px;
    font-size: 12px; line-height: 1.4;
    white-space: nowrap;
  }
  .contact .person { font-weight: 700; font-size: 16px; text-transform: uppercase; line-height: 1.2; }
  .contact .role { font-size: 13px; margin-bottom: 4px; }
  .gold-rule {
    position: absolute; left: 24px; width: 330px; bottom: 34px;
    height: 2px; background: var(--gold);
  }
</style>
</head>
<body>
  <section class="card card-front">
    <div class="brand-name">Joinolux</div>
    <div class="divider"></div>
    <div class="contact">
      <p class="person">Mark Tellman</p>
      <p class="role">Managing Director</p>
      <p>214 Harbor Mill Lane, Hampton Roads,</p>
      <p>Virginia United States</p>
      <p>(757) 348-2615</p>
      <p>joinolux-example.com</p>
      <p>mark@joinolux-example.com</p>
    </div>
    <div class="gold-rule"></div>
  </section>
  <section class="card card-back">
    <div class="brand-name">Joinolux</div>
  </section>
</body>
</html>
```